Audio Visual company needs brochure design

We are an AV company that does Audio Visual work solely for Commercial customers. We Design, sale and install various Audio Visual systems for our customers. This may be something as simple as a conference room, a new sound system for a church or a new sound, lighting and video system for an arena or stadium.

We don't really have any ideas in mind and that's the reason we are turning to you. We want something that highlights what we do, and something they will look at - not just toss in the can.

Included is a copy of our logo (sorry it's the only copy we have now)

Our company name is Velmira Staging www.velmirastaging.example
Updates

Reason: The rest of our management team hasn't provided feedback to me yet. We will pick the design this week.

Target Market(s)

70% of our business is churches and the remaining is corporate customers and restaurants.

Industry/Entity Type

Church

Requirements
Must have
• The brochure will be 8.5" x 11" printed both sides - open to Z fold or Tri fold designs. We can provide pictures of our work if needed - though they may not be the best.
Should not have
• No generic pictures of just speakers, projectors, microphones, etc.

```html
<!DOCTYPE html>
<html lang="en">
<head>
<meta charset="utf-8">
<title>Velmira Staging – Smart Solutions</title>
<link rel="stylesheet" href="https://fonts.googleapis.com/css2?family=Jost:wght@400;500;700&family=PT+Sans:wght@400;700&display=swap">
<style>
  :root {
    --page-bg: #e9e6e2;
    --paper: #ffffff;
    --brown-dark: #4a1d10;
    --brown-text: #3e1a0f;
    --red: #bd3a2c;
    --pink: #f4a39b;
    --white: #ffffff;
    --body-text: #3a2a24;
  }
  * { margin: 0; padding: 0; box-sizing: border-box; }
  html, body { width: 1006px; height: 1200px; overflow: hidden; background: var(--page-bg); }
  .flyer {
    position: absolute; left: 53px; top: 18px;
    width: 900px; height: 1163px;
    background: var(--paper); overflow: hidden;
    font-family: "PT Sans", sans-serif;
  }
  .flyer-shapes { position: absolute; inset: 0; }

  .tagline span {
    position: absolute; line-height: 1; white-space: nowrap;
    font-family: "Jost", sans-serif; font-weight: 400; color: var(--brown-text);
  }
  .tagline .word-innovation { left: 22px; top: 18px; font-size: 52px; }
  .tagline .word-motivation { left: 282px; top: 24px; font-size: 45px; }
  .tagline .word-satisfaction { left: 509px; top: 30px; font-size: 37px; }

  .speaker-photo {
    position: absolute; left: 529px; top: 497px; width: 268px; height: 302px;
    background: linear-gradient(160deg, #3a3a3c, #111 60%, #2b2b2d);
  }

  .hero-title {
    position: absolute; left: 34px; top: 346px;
    font-family: "Jost", sans-serif; font-size: 61px; font-weight: 400;
    color: var(--white); line-height: 1; white-space: nowrap;
  }
  .hero-title b { font-weight: 700; }
  .mission {
    position: absolute; left: 28px; top: 426px;
    font-size: 18px; line-height: 24px; color: var(--white); white-space: nowrap;
  }

  .services-title {
    position: absolute; left: 32px; top: 549px;
    font-family: "Jost", sans-serif; font-size: 41px; font-weight: 400;
    color: var(--brown-dark); line-height: 1; white-space: nowrap;
  }
  .services-title b { font-weight: 700; }
  .services-text {
    position: absolute; left: 32px; top: 606px;
    font-size: 20px; line-height: 26.5px; color: var(--white); white-space: nowrap;
  }

  .service-col { position: absolute; top: 820px; }
  .service-col.design { left: 357px; }
  .service-col.production { left: 625px; }
  .service-col h3 {
    font-family: "Jost", sans-serif; font-size: 21px; font-weight: 400; line-height: 28px;
    color: var(--red); white-space: nowrap; margin-bottom: 4px;
  }
  .service-col h3 b { font-weight: 700; }
  .service-col h3 .amp { font-size: 26px; color: var(--brown-dark); }
  .service-col p {
    font-size: 16px; line-height: 21.2px; color: var(--body-text); white-space: nowrap;
  }

  .brand-name {
    position: absolute; left: 66px; top: 1122px; line-height: 1;
    font-family: "PT Sans", sans-serif; font-weight: 700; font-size: 21px;
    color: var(--red); white-space: nowrap;
  }
  .web-address {
    position: absolute; left: 483px; top: 1119px; line-height: 1;
    font-family: "Jost", sans-serif; font-size: 24px; color: var(--brown-text);
    letter-spacing: 0.5px; white-space: nowrap;
  }
  .web-address b { color: var(--red); font-weight: 700; }
</style>
</head>
<body>
<main class="flyer">
  <svg class="flyer-shapes" viewBox="0 0 612 791" width="900" height="1163" preserveAspectRatio="none">
    <defs>
      <linearGradient id="conferenceTone" x1="0" y1="0" x2="1" y2="1">
        <stop offset="0" stop-color="#f3f3f4"/>
        <stop offset="0.45" stop-color="#c9c8cc"/>
        <stop offset="1" stop-color="#7a3a2c"/>
      </linearGradient>
    </defs>
    <rect class="conference-photo" x="0" y="0" width="612" height="360" fill="url(#conferenceTone)" role="img" aria-label="Photo of a conference table lined with gooseneck microphones"/>
    <polygon class="band-dark" points="0,173 340,238 450,358 0,358" fill="var(--brown-dark)"/>
    <polygon class="wedge-red-upper" points="440,350 612,282 612,350" fill="var(--red)"/>
    <polygon class="stripe-pink-upper" points="420,350 612,252 612,272 448,350" fill="var(--pink)"/>
    <rect class="band-dark-strip" x="0" y="348" width="612" height="14" fill="var(--brown-dark)"/>
    <polygon class="wedge-dark-right" points="455,361 612,361 612,398" fill="var(--brown-dark)"/>
    <polygon class="field-red" points="0,361 452,361 0,653" fill="var(--red)"/>
    <polygon class="stripe-pink-lower" points="0,653 452,361 476,361 0,695" fill="var(--pink)"/>
  </svg>

  <div class="speaker-photo" role="img" aria-label="Photo of a pair of black desktop speakers with yellow cones"></div>

  <div class="tagline">
    <span class="word-innovation">Innovation</span>
    <span class="word-motivation">Motivation</span>
    <span class="word-satisfaction">Satisfaction</span>
  </div>

  <h1 class="hero-title"><b>Smart</b>Solutions</h1>
  <p class="mission">OUR MISSION is to provide our customers with creative and<br>unique installation and production services within budget and on time.</p>

  <h2 class="services-title"><b>OUR</b>SERVICES</h2>
  <p class="services-text">We Design, sale and install various Audio Visual<br>systems for our customers. This may be<br>something as simple as a conference<br>room, a new sound system for a<br>church or a new sound, lighting<br>and video system for an<br>arena or stadium.</p>

  <section class="service-col design">
    <h3><b>DESIGN</b><span class="amp">&amp;</span>INSTALLATION</h3>
    <p>Our design &amp; installation team<br>accounts for a large portion of<br>our business. With some of the<br>best in the country on our staff,<br>Velmira has become a premier<br>systems integration company.<br>Clients like Harlow Trust,<br>Brightmere Capital, Quillora &amp;<br>Pennyworth Grill have called on<br>Velmira to design and install<br>AV systems critical to their day<br>to day operations.</p>
  </section>

  <section class="service-col production">
    <h3><b>PRODUCTION</b><span class="amp">&amp;</span>RENTALS</h3>
    <p>Serving the concert, theater and<br>corporate markets, Velmira<br>provides Sound, Lighting, Video &amp;<br>Staging services for our clients<br>events. We have a rental<br>department that is second to<br>none with reasonable rates, a<br>large inventory and a<br>knowledgeable rental staff.<br>Contact us and see why companies<br>like Kestrel Motors &amp; Northline<br>Review trust their image in our hands.</p>
  </section>

  <div class="brand-name">Velmira Staging</div>
  <div class="web-address">www.<b>velmirastaging</b>.example</div>
</main>
</body>
</html>
```